Plumbing Company After Business Card

Business card for a plumbing business that offers a variety of plumbing services including maintenance, domestic and commercial plumbing. My main focus is to offer high quality professional service. A logo on the card would be ideal. Any other questions feel free to email. Cheers

Looking for something modern and upmarket with preferably a matte black background

Business name is Keystone Plumbing and Gas

Industry/Entity Type

Plumbing

Contact Information for Business Card

Keystone Plumbing and Gas
Marcus Thornell
0427915368
14 Corrigan Road, Elmvale 3561
keystoneplumbing@mailbay.com.au
ABN 52 647 183 925

Font styles to use
Sans Serif

Colors
1b1b1b
ffffff
3377b5

Requirements
Must have
• Domestic
• Commercial
• Maintenance

```html
<!DOCTYPE html>
<html lang="en">
<head>
<meta charset="utf-8">
<title>Keystone Plumbing and Gas – Business Card</title>
<link rel="stylesheet" href="https://fonts.googleapis.com/css2?family=Oswald:wght@300;400&display=swap">
<style>
  :root {
    --page: #d9d6d1;
    --card: #1b1b1b;
    --card-deep: #050505;
    --mesh-glow: #2a3a52;
    --text: #ffffff;
    --text-soft: #d8d8d8;
    --accent: #3377b5;
  }
  * { margin: 0; padding: 0; box-sizing: border-box; }
  html, body {
    width: 1200px; height: 1200px; overflow: hidden;
    background: var(--page);
    font-family: "Oswald", "Arial Narrow", sans-serif;
  }
  .sheet {
    width: 1200px; height: 1200px;
    display: flex; flex-direction: column; align-items: center; justify-content: center;
    gap: 44px;
  }
  .card {
    position: relative;
    width: 880px; height: 536px;
    background: var(--card-deep);
    overflow: hidden;
    box-shadow: 0 10px 28px rgba(0,0,0,0.35);
    color: var(--text);
  }
  .card__texture {
    position: absolute; inset: 0;
    background: radial-gradient(ellipse 55% 70% at 50% 52%, var(--mesh-glow) 0%, var(--card) 45%, var(--card-deep) 100%);
  }
  .card--contact .card__texture {
    background: radial-gradient(ellipse 45% 75% at 48% 48%, var(--mesh-glow) 0%, var(--card) 50%, var(--card-deep) 100%);
  }

  /* Contact side */
  .contact {
    position: absolute; right: 64px; top: 70px;
    text-align: right;
    font-weight: 300;
    text-transform: uppercase;
  }
  .contact__name {
    font-size: 62px; font-weight: 400; letter-spacing: 2px; line-height: 1;
    color: var(--text-soft);
  }
  .contact__phone {
    margin-top: 40px;
    font-size: 46px; letter-spacing: 2px; line-height: 1;
  }
  .contact__details {
    margin-top: 56px;
    list-style: none;
    font-size: 25px; line-height: 1.5; letter-spacing: 0.5px;
  }

  /* Brand side */
  .brand {
    position: absolute; left: 0; right: 0; top: 120px;
    text-align: center;
    text-transform: uppercase;
    color: var(--text-soft);
    font-weight: 400;
  }
  .brand__name {
    font-size: 150px; line-height: 1; letter-spacing: 6px;
  }
  .brand__tagline {
    margin-top: 8px;
    font-size: 44px; letter-spacing: 2px; line-height: 1;
  }
  .services {
    position: absolute; left: 150px; right: 150px; top: 430px;
    display: flex; justify-content: space-between;
    list-style: none;
    text-transform: uppercase;
    font-size: 24px; font-weight: 400; letter-spacing: 0.5px;
    color: var(--text-soft);
  }
</style>
</head>
<body>
<main class="sheet">

  <section class="card card--contact" aria-label="Card back: contact details">
    <div class="card__texture" role="img" aria-label="Dark hexagonal metal mesh texture"></div>
    <div class="contact">
      <h1 class="contact__name">Marcus Thornell</h1>
      <p class="contact__phone">0427915368</p>
      <ul class="contact__details">
        <li>keystoneplumbing@mailbay.com.au</li>
        <li>14 Corrigan Road, Elmvale 3561</li>
        <li>ABN 52 647 183 925</li>
      </ul>
    </div>
  </section>

  <section class="card card--brand" aria-label="Card front: company name and services">
    <div class="card__texture" role="img" aria-label="Dark hexagonal metal mesh texture"></div>
    <div class="brand">
      <p class="brand__name">Keystone</p>
      <p class="brand__tagline">Plumbing and Gas</p>
    </div>
    <ul class="services">
      <li>Domestic</li>
      <li>Commercial</li>
      <li>Maintenance</li>
    </ul>
  </section>

</main>
</body>
</html>
```